Kx7Orbit WebSite

an educational website about tutoring, client will be surfing this site looking for a tutor, please see the attached images because the contains exactly what we need.
Updates

Project Deadline Extended Reason: something went wrong with the uploaded files, we are very sorry.thank you PlumeVault for the 5 days extension.now there is a 3 images describing the content of the three pages.good luck Added Friday, August 5, 2016

Target Market(s)

everyone

Industry/Entity Type

Education

Number of Pages Required

3 page

Font styles to use
Other font styles liked:
• something looks good in Arabic and english like "Droid Arabic Kufi"

Requirements
Must have
• the logo we attached, responsive design, simple, also try as much as you can Centering texts and layout because this website will have an Arabic version, Arabic is a Right-to-Left Language.
• a change language button,
Nice to have
• educational gestures.
• Centered texts and layout because this website will have an Arabic version, Arabic is a Right-to-Left Language.
• we have a web designer and we can download any template and add our logo and text to it, but.....
• we need creativity, so please stick to the contents in the images we attached, we need something very simple, more like a zorvia home page with little touch of filtering fields like the 5 dropdownlist and the gender selection buttons.
• try not to go far away from the contents we specified in the images, use less images or dont use images at all, try not to make the client scroll down,
Should not have
• too much colors or noisy layout or heavy media

```html
<!DOCTYPE html>
<html lang="en">
<head>
<meta charset="utf-8">
<title>Kx7Orbit – Find a Tutor</title>
<link href="https://fonts.googleapis.com/css2?family=Open+Sans:wght@400;600;700;800&family=Roboto+Condensed:wght@700&display=swap" rel="stylesheet">
<style>
:root{
  --blue:#1677c4;
  --sky:#29a8e0;
  --brand:#1a8ad4;
  --orange:#f7941d;
  --ink:#111111;
  --dark:#2b2b2b;
  --field:#eeeeee;
  --label:#333333;
  --white:#ffffff;
  --footer-bar:#1d1d1d;
}
*{margin:0;padding:0;box-sizing:border-box}
html,body{width:1138px;height:1200px;overflow:hidden;background:var(--white)}
body{position:relative;font-family:"Open Sans",sans-serif;color:var(--ink)}
.abs{position:absolute}

/* top strip */
.top-line{left:0;top:0;width:1138px;height:5px;background:var(--blue)}
.contact-bar{left:0;top:0;width:1138px;height:44px}
.contact-item{top:11px;color:var(--white);font-weight:600;font-size:15px;display:flex;align-items:center;gap:8px}
.socials{display:flex;gap:4px}
.social-dot{width:19px;height:19px;border:1.6px solid var(--white);border-radius:50%}

/* header */
.brand{left:29px;top:50px;display:flex;align-items:center;gap:12px}
.brand-square{width:62px;height:62px;background:var(--brand)}
.brand-name{font-weight:700;font-size:52px;color:var(--brand);letter-spacing:-1px}
.main-nav{top:96px;display:flex;gap:20px;font-family:"Roboto Condensed",sans-serif;font-size:16px;color:var(--ink)}
.main-nav .current{border-bottom:3px solid var(--sky);padding-bottom:3px}
.btn-login{left:912px;top:88px;width:88px;height:34px;background:var(--orange);color:var(--white);border-radius:3px;font-family:"Roboto Condensed",sans-serif;font-size:16px;display:flex;align-items:center;justify-content:center}
.btn-register{left:1009px;top:88px;width:89px;height:34px;border:1px solid #cfcfcf;border-radius:3px;font-family:"Roboto Condensed",sans-serif;font-size:16px;display:flex;align-items:center;justify-content:center}

/* section nav */
.section-nav{left:0;top:165px;width:1138px;height:49px;background:var(--sky)}
.section-nav span{position:absolute;top:15px;color:var(--white);font-family:"Roboto Condensed",sans-serif;font-size:16px}

/* hero */
.hero{left:0;top:214px;width:1138px;height:633px;background:linear-gradient(100deg,#8d96a2 0%,#b7bec6 30%,#a99d92 62%,#6f5a4c 85%,#4c3f37 100%)}
.hero-shade{left:0;top:214px;width:1138px;height:633px;background:linear-gradient(180deg,rgba(40,55,80,.25),rgba(40,55,80,.45))}
.hero-title{left:0;top:328px;width:1195px;text-align:center;color:var(--white);font-weight:800;font-size:31px;letter-spacing:-.3px}
.hero-title em{font-style:normal;color:var(--sky)}
.hero-lead{left:0;top:381px;width:1195px;text-align:center;color:var(--white);font-weight:600;font-size:16.5px;line-height:23px}

/* find a tutor panel */
.finder{left:61px;top:474px;width:1041px;height:258px;border:2px solid var(--white);border-radius:4px;background:rgba(22,105,185,.82)}
.finder-icon{left:36px;top:450px}
.finder-title{left:132px;top:509px;color:var(--white);font-size:28px;font-weight:400}
.btn-listings{left:825px;top:496px;width:246px;height:34px;background:var(--ink);border-radius:3px;color:var(--white);font-family:"Roboto Condensed",sans-serif;font-size:15px;display:flex;align-items:center;justify-content:center;gap:12px}
.finder-form{left:75px;top:552px;width:1013px;height:165px;background:var(--white);border-radius:4px}
.field-label{font-size:13.5px;font-weight:600;color:var(--label)}
.select{height:39px;background:var(--field);border-radius:2px;font-size:14px;color:#555;padding-left:13px;display:flex;align-items:center}
.select::after{content:"";position:absolute;right:12px;top:16px;border-left:8px solid transparent;border-right:8px solid transparent;border-top:8px solid #444}
.btn-search{left:756px;top:663px;width:321px;height:39px;background:var(--dark);border-radius:3px;color:var(--white);font-family:"Roboto Condensed",sans-serif;font-size:16px;display:flex;align-items:center;justify-content:center;gap:12px}

/* footer */
.footer{left:0;top:847px;width:1138px;height:321px;background:var(--blue)}
.footer-heading{top:906px;color:var(--white);font-weight:700;font-size:16px}
.footer-rule{top:928px;height:2px;background:rgba(255,255,255,.75)}
.footer-links{top:951px;color:var(--white);font-weight:600;font-size:13.5px;line-height:20.9px}
.news-input{left:530px;width:234px;height:29px;background:var(--ink);border-radius:2px;color:var(--white);font-size:11px;font-weight:700;padding-left:13px;display:flex;align-items:center}
.news-submit{left:530px;top:1017px;width:104px;height:29px;background:var(--ink);border-radius:2px;color:var(--white);font-weight:700;font-size:14px;display:flex;align-items:center;justify-content:center}
.footer-brand{left:862px;top:978px;display:flex;align-items:center;gap:10px}
.footer-brand-square{width:46px;height:46px;background:var(--white)}
.footer-brand-name{color:var(--white);font-weight:700;font-size:40px;letter-spacing:-1px}
.legal-bar{left:0;top:1168px;width:1138px;height:32px;background:var(--footer-bar)}
.legal-text{left:32px;top:1177px;color:var(--white);font-weight:700;font-size:11px}
.legal-socials{left:1040px;top:1174px;display:flex;gap:4px}
.legal-socials .social-dot{background:var(--white);border:none}
</style>
</head>
<body>

<!-- contact strip -->
<svg class="abs contact-bar" width="1138" height="44" viewBox="0 0 1138 44">
  <polygon points="555,0 1138,0 1100,44 596,44" fill="#1677c4"/>
</svg>
<div class="abs top-line"></div>
<div class="abs contact-item" style="left:628px">
  <svg width="24" height="24" viewBox="0 0 24 24"><circle cx="12" cy="12" r="10.5" fill="none" stroke="#fff" stroke-width="1.6"/><path d="M8.5 7.5l2 2-1 1.3c.8 1.6 2 2.8 3.7 3.7l1.3-1 2 2-1.3 1.5c-3.5-.5-7.2-4.2-7.7-7.7z" fill="#fff"/></svg>
  1-800-555-0142
</div>
<div class="abs contact-item" style="left:807px">
  <svg width="24" height="24" viewBox="0 0 24 24"><circle cx="12" cy="12" r="10.5" fill="none" stroke="#fff" stroke-width="1.6"/><rect x="7" y="8.5" width="10" height="7" fill="none" stroke="#fff" stroke-width="1.4"/><path d="M7 8.5l5 4 5-4" fill="none" stroke="#fff" stroke-width="1.4"/></svg>
  info@kx7orbit.com
</div>
<div class="abs socials" style="left:994px;top:13px">
  <span class="social-dot"></span><span class="social-dot"></span><span class="social-dot"></span>
</div>

<!-- header -->
<div class="abs brand"><span class="brand-square"></span><span class="brand-name">Kx7Orbit</span></div>
<nav class="abs main-nav" style="left:699px">
  <span class="current">HOME</span><span>ABOUT</span><span>CONTACT</span>
</nav>
<div class="abs btn-login">LOGIN</div>
<div class="abs btn-register">REGISTER</div>

<!-- section nav -->
<nav class="abs section-nav">
  <span style="left:301px">SEARCH</span>
  <span style="left:402px">FOR STUDENTS ⌄</span>
  <span style="left:556px">FOR TUTORS ⌄</span>
  <span style="left:695px">FAQ</span>
  <span style="left:772px">RESOURCE</span>
</nav>

<!-- hero -->
<div class="abs hero" role="img" aria-label="Photo of a tutor and a smiling student working together on a tablet on a sofa"></div>
<div class="abs hero-shade"></div>
<h1 class="abs hero-title">WE HELP YOU TO FIND <em>A GREAT TUTOR</em> IN YOUR AREA!</h1>
<p class="abs hero-lead">Kx7Orbit.com is a faster, easier way to find a tutor. We have more than 100,000 tutors<br>in 4500 cities all over the world you can contact for FREE!</p>

<!-- finder -->
<section class="abs finder"></section>
<svg class="abs finder-icon" width="92" height="80" viewBox="0 0 92 80">
  <circle cx="35" cy="35" r="33" fill="#1677c4"/>
  <circle cx="35" cy="35" r="18" fill="none" stroke="#fff" stroke-width="7"/>
  <line x1="49" y1="49" x2="70" y2="70" stroke="#fff" stroke-width="9" stroke-linecap="round"/>
</svg>
<h2 class="abs finder-title">FIND A TUTOR</h2>
<div class="abs btn-listings">
  <svg width="36" height="22" viewBox="0 0 36 22"><g fill="#fff"><rect x="0" y="0" width="5" height="4"/><rect x="0" y="9" width="5" height="4"/><rect x="0" y="18" width="5" height="4"/><rect x="9" y="0" width="27" height="4"/><rect x="9" y="9" width="27" height="4"/><rect x="9" y="18" width="27" height="4"/></g></svg>
  VIEW ALL LISTINGS
</div>
<div class="abs finder-form"></div>

<span class="abs field-label" style="left:88px;top:571px">SELECT A SUBJECT</span>
<span class="abs field-label" style="left:423px;top:571px">LEVEL</span>
<span class="abs field-label" style="left:759px;top:571px">POSTAL CODE</span>
<div class="abs select" style="left:85px;top:586px;width:321px">ACADEMIC</div>
<div class="abs select" style="left:420px;top:586px;width:321px">ALL LEVELS</div>
<div class="abs" style="left:756px;top:586px;width:321px;height:39px;background:var(--field);border-radius:2px"></div>

<span class="abs field-label" style="left:88px;top:648px">SUBJECT DETAIL</span>
<span class="abs field-label" style="left:423px;top:648px">TYPE</span>
<div class="abs select" style="left:85px;top:663px;width:321px">SELECT</div>
<div class="abs select" style="left:420px;top:663px;width:321px">ONE ON ONE</div>
<div class="abs btn-search">
  <svg width="26" height="22" viewBox="0 0 26 22"><g fill="#fff"><circle cx="5" cy="5" r="3"/><circle cx="12" cy="4" r="3"/><path d="M0 14c0-4 2-6 5-6s4 2 4 4z"/><path d="M7 12c0-4 2-5 5-5s5 2 5 4z"/></g><circle cx="18" cy="14" r="4" fill="none" stroke="#fff" stroke-width="1.6"/><line x1="21" y1="17" x2="24" y2="20" stroke="#fff" stroke-width="1.8"/></svg>
  SEARCH TUTOR
</div>

<!-- footer -->
<footer class="abs footer"></footer>
<h3 class="abs footer-heading" style="left:81px">QUICK LINKS</h3>
<div class="abs footer-rule" style="left:78px;width:109px"></div>
<ul class="abs footer-links" style="left:80px;list-style:none">
  <li>SEARCH</li><li>FOR STUDENTS</li><li>FOR TUTORS</li><li>FAQ</li><li>RESOURCE</li><li>LOCATIONS</li><li>ABOUT</li><li>CONTACT</li>
</ul>
<h3 class="abs footer-heading" style="left:283px">TUTORS</h3>
<div class="abs footer-rule" style="left:282px;width:154px"></div>
<ul class="abs footer-links" style="left:283px;list-style:none">
  <li>BROWSE BY SUBJECT</li><li>BROWSE BY LOCATION</li>
</ul>
<h3 class="abs footer-heading" style="left:533px">SUBSCRIBE FOR NEWSLETTER</h3>
<div class="abs footer-rule" style="left:531px;width:234px"></div>
<div class="abs news-input" style="top:949px">NAME</div>
<div class="abs news-input" style="top:983px">EMAIL</div>
<div class="abs news-submit">SUBMIT</div>
<div class="abs footer-brand"><span class="footer-brand-square"></span><span class="footer-brand-name">Kx7Orbit</span></div>

<div class="abs legal-bar"></div>
<p class="abs legal-text">COPYRIGHT © 2016 KX7ORBIT. ALL RIGHTS RESERVED.</p>
<div class="abs legal-socials"><span class="social-dot"></span><span class="social-dot"></span><span class="social-dot"></span></div>

</body>
</html>
```